Real estate broker business card

Want a modern celan but effective business card for my residential and commercial real estate business. I want the back of the card to advertise my services and to capture business. I have attached the back of my current business card fore ideas
Updates

Target Market(s)

home buyers and seller. commercial buyers and sellers

Industry/Entity Type

Real Estate

Contact Information for Business Card

must have my contact information and my photo

Requirements
Must have
• Lorna Vettridge
• Owner & Qualifying Broker
• Brockhill Real Estate Services
• 555.218.7094
• lorna@brockhillhomes.example
• www.brockhillhomes.example
Nice to have
• metallic
• Business capture text: " Don't buy or lease property without someone looking out for your best interests. I will represent you on your home or investment purchase for FREE!"
• "Home owners, call today to receive a FREE market analysis for your homes value!

```html
<!DOCTYPE html>
<html lang="en">
<head>
<meta charset="utf-8">
<title>Brockhill Real Estate Services – Business Card</title>
<link href="https://fonts.googleapis.com/css2?family=Source+Sans+3:ital,wght@0,400;0,600;1,400&display=swap" rel="stylesheet">
<style>
  :root {
    --stage-bg: #ededee;
    --card-front-bg: #e3e4e6;
    --card-back-bg: #ffffff;
    --teal: #1a7c8c;
    --teal-dark: #0f6472;
    --text-grey: #4a4d50;
    --muted-grey: #6d7073;
    --photo-hair: #2a1d18;
    --photo-skin: #c99a80;
    --photo-blouse: #e9e6e3;
  }
  * { box-sizing: border-box; margin: 0; padding: 0; }
  html, body {
    width: 1200px; height: 900px; overflow: hidden;
    background: var(--stage-bg);
    font-family: "Source Sans 3", "Helvetica Neue", Arial, sans-serif;
  }
  .stage { position: relative; width: 1200px; height: 900px; }

  .card {
    position: absolute;
    width: 556px; height: 343px;
    overflow: hidden;
    box-shadow: 0 6px 18px rgba(0,0,0,.12);
  }
  .card--front { left: 238px; top: 62px; background: var(--card-front-bg); }
  .card--back  { left: 457px; top: 518px; background: var(--card-back-bg); }

  /* portrait area */
  .portrait {
    position: absolute; left: 0; top: 26px; width: 246px; bottom: 0;
    border-radius: 110px 120px 0 0;
    background: linear-gradient(180deg,
      var(--photo-hair) 0%, var(--photo-hair) 18%,
      var(--photo-skin) 34%, var(--photo-skin) 55%,
      var(--photo-hair) 62%, var(--photo-blouse) 74%, var(--photo-blouse) 100%);
  }

  /* brand lockup */
  .brand { position: absolute; display: flex; align-items: center; gap: 12px; }
  .brand__mark { background: var(--teal); flex: none; }
  .brand__name {
    color: var(--teal); font-weight: 600; line-height: 1.05;
  }
  .card--front .brand { left: 276px; top: 52px; }
  .card--front .brand__mark { width: 62px; height: 62px; }
  .card--front .brand__name { font-size: 26px; }
  .card--back .brand { left: 34px; top: 30px; }
  .card--back .brand__mark { width: 86px; height: 86px; }
  .card--back .brand__name { font-size: 35px; }

  /* contact block */
  .identity {
    position: absolute; right: 28px; top: 164px; text-align: right;
  }
  .identity__name { color: var(--teal); font-weight: 600; font-size: 19px; line-height: 1.2; }
  .identity__title { color: var(--text-grey); font-size: 15.5px; line-height: 1.3; }

  .contacts {
    position: absolute; right: 28px; top: 242px; list-style: none; text-align: right;
  }
  .contacts li {
    display: flex; justify-content: flex-end; align-items: center; gap: 9px;
    color: var(--text-grey); font-size: 15px; line-height: 20px;
  }
  .contacts svg { width: 11px; height: 11px; fill: var(--teal); flex: none; }

  /* back copy */
  .pitch {
    position: absolute; left: 33px; top: 164px; width: 330px;
    color: var(--teal-dark); font-size: 15.5px; line-height: 20px;
  }
  .offer {
    position: absolute; left: 33px; top: 258px; width: 320px;
    color: var(--muted-grey); font-style: italic; font-size: 15px; line-height: 20px;
  }
</style>
</head>
<body>
<main class="stage">

  <section class="card card--front" aria-label="Business card front">
    <div class="portrait" role="img" aria-label="Portrait photo of Lorna Vettridge"></div>

    <div class="brand">
      <span class="brand__mark" aria-hidden="true"></span>
      <span class="brand__name">Brockhill<br>Real Estate Services</span>
    </div>

    <div class="identity">
      <p class="identity__name">Lorna Vettridge</p>
      <p class="identity__title">Owner &amp; Qualifying Broker</p>
    </div>

    <ul class="contacts">
      <li>555.218.7094
        <svg viewBox="0 0 24 24" aria-hidden="true"><path d="M6.6 10.8a15.1 15.1 0 0 0 6.6 6.6l2.2-2.2a1 1 0 0 1 1-.25 11.4 11.4 0 0 0 3.6.57 1 1 0 0 1 1 1V20a1 1 0 0 1-1 1A17 17 0 0 1 3 4a1 1 0 0 1 1-1h3.5a1 1 0 0 1 1 1c0 1.25.2 2.45.57 3.57a1 1 0 0 1-.25 1z"/></svg>
      </li>
      <li>lorna@brockhillhomes.example
        <svg viewBox="0 0 24 24" aria-hidden="true"><path d="M2 5h20v14H2z" fill="none"/><path d="M2 5h20v2l-10 6L2 7zM2 9l10 6 10-6v10H2z"/></svg>
      </li>
      <li>www.brockhillhomes.example
        <svg viewBox="0 0 24 24" aria-hidden="true"><circle cx="12" cy="12" r="10"/><path d="M2 12h20M12 2c3 3 3 17 0 20M12 2c-3 3-3 17 0 20" stroke="#e3e4e6" stroke-width="1.6" fill="none"/></svg>
      </li>
    </ul>
  </section>

  <section class="card card--back" aria-label="Business card back">
    <div class="brand">
      <span class="brand__mark" aria-hidden="true"></span>
      <span class="brand__name">Brockhill<br>Real Estate Services</span>
    </div>

    <p class="pitch">Don't buy or lease property without someone looking out for your best interests. I will represent you on your home or investment purchase for FREE!</p>
    <p class="offer">Home owners, call today to receive a FREE market analysis for your homes value!</p>
  </section>

</main>
</body>
</html>
```